Business card: GREEN HERONS TRADE SUPPLY

Hello,

This is your mission:

-I've just done my logo on the website. Now, I need A BUSINESS CARD.
-2 same business cards for 2 persons
-Landscape
-Dimension of the business card: 8.5 cm long and 5 cm high
-Different front and back
-For your information: this new company is selling products (fashion accessories, electronics, watches, fragrances, sunglasses, etc. to large clients related to shops in airlines (inflight catalogue), airports, cruises, etc.
-Colors and logo: please use the same colors of the logo attached (in blue with orange details) and follow the spirit of the existing logo.

-Front:
-1st person:
GREEN HERONS s.p.r.l.
Travel Retail Agency
www.greenheronsx.com
Lucien DEMARBAIX
Partner
Mobile: +32488316257
Email: ld@greenheronsx.com
-2nd person:
GREEN HERONS s.p.r.l.
Travel Retail Agency
www.greenheronsx.com
Joris VANMECHELEN
Partner
Mobile: +32488625170
Email: jv@greenheronsx.com

-Back
Logo
see attached file. Please use the colors of the logo in blue with orange details.

Reason: I increase time necause i don t know if the deadline is in usa time or european time. I will make the selection at 9pm belgian time.

I'm selling products to large accounts/clients. Some of them do more than 2 Billion eur turnover

Airlines

Must have
• Use the logo.
The buyers get so many business cards.
They should remember me easily.
This is why my logo/company name is a stork and a color. 2 things that people usually remember easily.

```html
<!DOCTYPE html>
<html lang="en">
<head>
<meta charset="utf-8">
<title>Green Herons Trade Supply: Business Card</title>
<link rel="stylesheet" href="https://fonts.googleapis.com/css2?family=Didact+Gothic&display=swap">
<style>
  :root {
    --page-bg: #d9dadc;
    --sky-teal: #1b9cc6;
    --deep-blue: #1d4e8c;
    --wave-blue: #2a6fa8;
    --accent-orange: #f08a24;
    --soft-white: #eef4fa;
    --cream: #fdfbe8;
    --logo-teal: #1e8fb3;
  }
  * { margin: 0; padding: 0; box-sizing: border-box; }
  html, body {
    width: 1200px;
    height: 720px;
    overflow: hidden;
    background: var(--page-bg);
    font-family: "Didact Gothic", "Century Gothic", sans-serif;
  }
  .card-sheet {
    position: relative;
    width: 1200px;
    height: 720px;
  }
  .card {
    position: absolute;
    top: 201px;
    width: 540px;
    height: 318px;
    overflow: hidden;
    box-shadow: 0 6px 18px rgba(0, 0, 0, 0.25);
  }

  /* Front */
  .card-front {
    left: 45px;
    background: var(--sky-teal);
  }
  .card-front .wave {
    position: absolute;
    inset: 0;
    width: 100%;
    height: 100%;
  }
  .company-name {
    position: absolute;
    left: 22px;
    top: 24px;
    font-size: 31px;
    color: var(--accent-orange);
    letter-spacing: 0.5px;
  }
  .company-tagline {
    position: absolute;
    left: 200px;
    top: 72px;
    font-size: 15px;
    color: var(--accent-orange);
  }
  .person-name {
    position: absolute;
    left: 222px;
    top: 124px;
    font-size: 22px;
    color: var(--accent-orange);
  }
  .person-role {
    position: absolute;
    left: 306px;
    top: 155px;
    font-size: 14px;
    color: var(--soft-white);
  }
  .website {
    position: absolute;
    left: 248px;
    top: 232px;
    font-size: 15px;
    color: var(--soft-white);
  }
  .contact-line {
    position: absolute;
    left: 22px;
    bottom: 22px;
    font-size: 13.5px;
    color: var(--soft-white);
    white-space: nowrap;
  }
  .contact-line span + span { margin-left: 12px; }

  /* Back */
  .card-back {
    left: 615px;
    background: var(--cream);
  }
  .card-back .corner {
    position: absolute;
    width: 0;
    height: 0;
  }
  .corner-top-right {
    top: 0;
    right: 0;
    border-top: 46px solid var(--accent-orange);
    border-left: 46px solid transparent;
  }
  .corner-bottom-left {
    bottom: 0;
    left: 0;
    border bottom: 0;
    border-bottom: 46px solid var(--accent-orange);
    border-right: 46px solid transparent;
  }
  .brand-lockup {
    position: absolute;
    left: 0;
    right: 0;
    top: 110px;
    display: flex;
    align-items: center;
    justify-content: center;
    gap: 16px;
  }
  .brand-dot {
    width: 30px;
    height: 30px;
    border-radius: 50%;
    background: var(--logo-teal);
    flex: none;
  }
  .brand-name {
    font-size: 30px;
    line-height: 1.15;
    color: var(--logo-teal);
    letter-spacing: 2px;
  }
</style>
</head>
<body>
<main class="card-sheet">

  <section class="card card-front" aria-label="Business card front">
    <svg class="wave" viewBox="0 0 540 318" preserveAspectRatio="none" aria-hidden="true">
      <path d="M0,200 C150,170 330,120 540,70 L540,318 L0,318 Z" fill="var(--wave-blue)"/>
      <path d="M0,214 C170,180 340,135 540,92 L540,318 L0,318 Z" fill="var(--deep-blue)"/>
    </svg>
    <h1 class="company-name">GREEN HERONS s.p.r.l.</h1>
    <p class="company-tagline">Travel Retail Agency</p>
    <p class="person-name">Lucien DEMARBAIX</p>
    <p class="person-role">Partner</p>
    <p class="website">www.greenheronsx.com</p>
    <p class="contact-line"><span>Mobile: +32488316257</span><span>Email: ld@greenheronsx.com</span></p>
  </section>

  <section class="card card-back" aria-label="Business card back">
    <div class="corner corner-top-right"></div>
    <div class="corner corner-bottom-left"></div>
    <div class="brand-lockup">
      <span class="brand-dot" aria-hidden="true"></span>
      <p class="brand-name">GREEN HERONS<br>TRADE SUPPLY</p>
    </div>
  </section>

</main>
</body>
</html>
```